Engineering group involved with fire safety needs a business card

We need a business card design for a company based in Greece called "Varotis Group". We are engineers and specialized technicians, operating the following : a) Fire fighting equipment trade b) Installation , Inspection & Maintenance of fire extinguishers and fire protection systems c) Occupational Health & Safety (Risk assessment & management/ Staff training). We need a clear and simple card design. I uploaded a draft I made, in order to give you an idea of the company and how I currently imagine the design of the card. I also uploaded the logo in .png file format. We are always open to different, new suggestions and ideas you may want to submit.
Target Market(s)
industries, companies, managers, retail clients
Industry/Entity Type
Fire Safety
Contact Information for Business Card
Addresses & phone numbers (headquarters + branch), logo, name (you can find all the details on the uploaded files!)
Colors
Designer to choose colors to be used in the design.
Look and feel
Each slider illustrates characteristics of the customer's brand and the style your logo design should communicate.

```html
<!DOCTYPE html>
<html lang="en">
<head>
<meta charset="utf-8">
<title>Varotis Group – Business Card</title>
<link href="https://fonts.googleapis.com/css2?family=Montserrat:wght@700;800&family=Roboto:wght@400;500;700&display=swap" rel="stylesheet">
<style>
  :root {
    --bg: #2b2b2d;
    --card: #232325;
    --card-shade: #28282a;
    --red: #c4161c;
    --white: #ffffff;
    --grey: #d9d9d9;
    --rule: #cfcfcf;
  }
  * { box-sizing: border-box; margin: 0; padding: 0; }
  html, body { width: 1200px; height: 1108px; overflow: hidden; }
  body {
    background: var(--bg);
    font-family: "Roboto", Arial, sans-serif;
    display: flex;
    justify-content: center;
    align-items: center;
    gap: 80px;
  }
  .card {
    width: 460px;
    height: 720px;
    border-radius: 22px;
    background: linear-gradient(160deg, var(--card-shade) 0%, var(--card) 60%);
    color: var(--white);
    display: flex;
    flex-direction: column;
    align-items: center;
    padding: 110px 44px 60px;
    box-shadow: 0 20px 40px rgba(0,0,0,.35);
  }
  .brand { display: flex; flex-direction: column; align-items: center; }
  .brand-mark {
    width: 56px; height: 56px;
    background: var(--red);
    margin-bottom: 22px;
  }
  .brand-name {
    font-family: "Montserrat", Arial, sans-serif;
    font-weight: 800;
    font-size: 46px;
    letter-spacing: 2px;
    line-height: 1;
    color: var(--red);
    text-align: center;
  }
  .brand-rule {
    width: 300px;
    height: 2px;
    background: var(--white);
    margin: 14px 0 10px;
  }
  .tagline {
    font-size: 19px;
    font-weight: 400;
    color: var(--grey);
    letter-spacing: .3px;
  }
  .person { margin-top: 50px; text-align: center; }
  .person-name {
    font-family: "Montserrat", Arial, sans-serif;
    font-weight: 700;
    font-size: 26px;
    color: var(--red);
    letter-spacing: .5px;
  }
  .person-title { font-size: 16px; font-weight: 500; margin-top: 6px; }
  .divider { width: 260px; height: 1px; background: var(--rule); margin: 20px 0; }
  .contact { font-size: 15px; line-height: 1.6; text-align: center; }
  .label { color: var(--red); }
  .services {
    margin-top: 70px;
    text-align: center;
    font-weight: 700;
    font-size: 17px;
    line-height: 1.75;
    letter-spacing: .4px;
  }
  .web { margin-top: auto; text-align: center; font-size: 20px; line-height: 1.5; }
  .web-url { color: var(--red); }
</style>
</head>
<body>

  <section class="card card-front">
    <div class="brand">
      <div class="brand-mark"></div>
      <div class="brand-name">VAROTIS GROUP</div>
      <div class="brand-rule"></div>
      <div class="tagline">installation - inspection - maintenance</div>
    </div>

    <div class="person">
      <div class="person-name">NIKOLAS VAROTIS</div>
      <div class="person-title">Mechanical Engineer - OHS Consultant</div>
    </div>

    <div class="divider"></div>
    <div class="contact">
      <div><span class="label">M.</span> +30 690 412 58 03</div>
      <div><span class="label">E.</span> nikolas.varotis@varotisgroup.gr</div>
    </div>
    <div class="divider"></div>

    <div class="contact">
      <div><span class="label">Headquarters:</span> 12 Agiou Nikolaou, 19500 Lavrio</div>
      <div><span class="label">T.</span> +30 22920 41180</div>
      <div><span class="label">Branch Office:</span> 18 Eleftherias Ave, 15124 Marousi</div>
      <div><span class="label">T.</span> +30 210 5550142</div>
    </div>
  </section>

  <section class="card card-back">
    <div class="brand">
      <div class="brand-mark"></div>
      <div class="brand-name">VAROTIS GROUP</div>
      <div class="brand-rule"></div>
      <div class="tagline">installation - inspection - maintenance</div>
    </div>

    <ul class="services" style="list-style:none">
      <li>FIRE FIGHTING EQUIPMENT</li>
      <li>LICENSING &amp; BUSINESS REGISTRATION</li>
      <li>OCCUPATIONAL HEALTH &amp; SAFETY</li>
      <li>STAFF TRAINING</li>
    </ul>

    <div class="web">
      <div>info@varotisgroup.gr</div>
      <div class="web-url">www.varotisgroup.gr</div>
    </div>
  </section>

</body>
</html>
```